Conceptual Model Diagram for Replacing Medication with Behavior to Support Weight Loss Maintenance

Design a figure of a conceptual model that needs to be inserted into a word document for a QDV grant. This conceptual model illustrates how behavioral strategies can replace the regulatory functions lost after AOM discontinuation. The intervention targets three core vulnerabilities—appetite resurgence, metabolic inflexibility, and suboptimal mindstate—through the domains of Food, Physical Activity, and Mind. Sustained weight loss maintenance occurs at the intersection of these domains. The intervention is delivered within a design framework that makes behaviors easier to perform, aligns them with identity, and reinforces them through virtual support and community, ensuring real-world feasibility and long-term adherence.
Target Market(s)
QDV reviewers
Industry/Entity Type
academic
Font styles to use
Other font styles liked:
- arial
Requirements
Must have
- see my attached description

```html
<!DOCTYPE html>
<html lang="en">
<head>
<meta charset="utf-8">
<title>Conceptual Model for Replacing Medication with Behavior to Support Weight Loss Maintenance</title>
<link rel="stylesheet" href="https://fonts.googleapis.com/css2?family=Anton&family=Arimo:ital,wght@0,400;0,700;1,700&display=swap">
<style>
  :root {
    --bg-light: #ffffff;
    --bg-shade: #f0f0f0;
    --ink: #000000;
    --paper: #ffffff;
    --identity-blue: #29a8e0;
    --easy-green: #3bb54a;
    --support-teal: #00a99d;
    --food-green: #3bb54a;
    --activity-blue: #29a8e0;
    --mind-teal: #00a99d;
    --food-activity: #0b7a42;
    --food-mind: #03772c;
    --activity-mind: #06728a;
    --core: #064a2c;
  }
  html, body {
    margin: 0;
    padding: 0;
    width: 1200px;
    height: 927px;
    overflow: hidden;
  }
  body {
    background: linear-gradient(90deg, var(--bg-light) 0%, var(--bg-light) 45%, var(--bg-shade) 100%);
  }
  .model {
    display: block;
    width: 1200px;
    height: 927px;
  }
  .title {
    font-family: "Anton", "Arial Narrow", sans-serif;
    font-size: 62px;
    fill: var(--ink);
  }
  .ring-label {
    font-family: "Arimo", Arial, sans-serif;
    font-weight: 700;
    font-size: 34px;
    fill: var(--paper);
  }
  .ring-note {
    font-family: "Arimo", Arial, sans-serif;
    font-weight: 400;
    font-size: 18px;
    fill: var(--paper);
  }
  .domain-label {
    font-family: "Arimo", Arial, sans-serif;
    font-weight: 700;
    font-size: 25px;
    fill: var(--paper);
    text-anchor: middle;
  }
  .vulnerability-box { fill: var(--ink); }
  .vulnerability-text {
    font-family: "Arimo", Arial, sans-serif;
    font-size: 16px;
    fill: var(--paper);
    text-anchor: middle;
  }
  .pointer {
    stroke: var(--ink);
    stroke-width: 2;
    fill: none;
  }
  .outcome {
    font-family: "Arimo", Arial, sans-serif;
    font-weight: 700;
    font-style: italic;
    font-size: 24px;
    fill: var(--ink);
    text-anchor: middle;
  }
  .domain-outline {
    fill: none;
    stroke: var(--ink);
    stroke-width: 1.5;
  }
</style>
</head>
<body>
<svg class="model" viewBox="0 0 1500 1159" xmlns="http://www.w3.org/2000/svg" role="img" aria-label="Conceptual model diagram">
  <defs>
    <marker id="arrowhead" viewBox="0 0 10 10" refX="9" refY="5" markerWidth="7" markerHeight="7" orient="auto">
      <path d="M0,0 L10,5 L0,10 z" fill="#000"/>
    </marker>
    <clipPath id="clip-food"><circle cx="753" cy="596" r="133"/></clipPath>
    <clipPath id="clip-activity"><circle cx="667" cy="730" r="133"/></clipPath>
    <clipPath id="clip-mind"><circle cx="834" cy="730" r="133"/></clipPath>

    <path id="arc-identity" d="M 405.4 859 A 398 398 0 0 1 750 262"/>
    <path id="arc-easy" d="M 750 298 A 362 362 0 0 1 1063.5 841"/>
    <path id="arc-identity-inner" d="M 436.5 841 A 362 362 0 0 1 750 298"/>
    <path id="arc-support" d="M 420.9 850 A 380 380 0 0 0 1079.1 850"/>
    <path id="arc-support-note" d="M 406.2 858.5 A 397 397 0 0 0 1093.8 858.5"/>
  </defs>

  <!-- Title -->
  <text class="title" x="751" y="142" text-anchor="middle" textLength="946" lengthAdjust="spacingAndGlyphs">Conceptual Model for Replacing Medication</text>
  <text class="title" x="751" y="203" text-anchor="middle" textLength="1106" lengthAdjust="spacingAndGlyphs">with Behavior to Support Weight Loss Maintenance</text>

  <!-- Framework ring -->
  <g class="framework-ring" fill="none" stroke-width="56">
    <path d="M 750 288 A 372 372 0 0 1 1072.2 846" stroke="var(--easy-green)"/>
    <path d="M 1072.2 846 A 372 372 0 0 1 427.8 846" stroke="var(--support-teal)"/>
    <path d="M 427.8 846 A 372 372 0 0 1 750 288" stroke="var(--identity-blue)"/>
  </g>

  <!-- Ring labels -->
  <text>
    <textPath href="#arc-identity-inner" startOffset="50%" text-anchor="middle"><tspan class="ring-label">Align with Identity</tspan><tspan class="ring-note">(self-concept, Maintain IT model, internalization)</tspan></textPath>
  </text>
  <text>
    <textPath href="#arc-easy" startOffset="50%" text-anchor="middle"><tspan class="ring-label">Make it Easy </tspan><tspan class="ring-note">(habits, routines, environment, low friction)</tspan></textPath>
  </text>
  <text class="ring-label">
    <textPath href="#arc-support" startOffset="50%" text-anchor="middle">Virtual Support and Social Connection</textPath>
  </text>
  <text class="ring-note">
    <textPath href="#arc-support-note" startOffset="50%" text-anchor="middle">(accessibility, community, shared accountability)</textPath>
  </text>

  <!-- Domains -->
  <g class="domains">
    <circle cx="753" cy="596" r="133" fill="var(--food-green)"/>
    <circle cx="667" cy="730" r="133" fill="var(--activity-blue)"/>
    <circle cx="834" cy="730" r="133" fill="var(--mind-teal)"/>
    <circle cx="667" cy="730" r="133" fill="var(--food-activity)" clip-path="url(#clip-food)"/>
    <circle cx="834" cy="730" r="133" fill="var(--food-mind)" clip-path="url(#clip-food)"/>
    <circle cx="834" cy="730" r="133" fill="var(--activity-mind)" clip-path="url(#clip-activity)"/>
    <g clip-path="url(#clip-food)">
      <g clip-path="url(#clip-activity)">
        <circle cx="834" cy="730" r="133" fill="var(--core)"/>
      </g>
    </g>
    <circle class="domain-outline" cx="753" cy="596" r="133"/>
    <circle class="domain-outline" cx="667" cy="730" r="133"/>
    <circle class="domain-outline" cx="834" cy="730" r="133"/>

    <text class="domain-label" x="753" y="571">Food</text>
    <text class="domain-label" x="619" y="752">Physical</text>
    <text class="domain-label" x="619" y="782">Activity</text>
    <text class="domain-label" x="875" y="776">Mind</text>
  </g>

  <!-- Vulnerabilities -->
  <g class="vulnerabilities">
    <rect class="vulnerability-box" x="685" y="357" width="131" height="45" rx="5"/>
    <text class="vulnerability-text" x="750" y="375">Appetite</text>
    <text class="vulnerability-text" x="750" y="395">Resurgence</text>
    <line class="pointer" x1="750" y1="412" x2="750" y2="466" marker-end="url(#arrowhead)"/>

    <rect class="vulnerability-box" x="451" y="523" width="131" height="46" rx="5"/>
    <text class="vulnerability-text" x="516" y="542">Metabolic</text>
    <text class="vulnerability-text" x="516" y="562">Inflexibility</text>
    <line class="pointer" x1="512" y1="580" x2="561" y2="627" marker-end="url(#arrowhead)"/>

    <rect class="vulnerability-box" x="921" y="523" width="132" height="46" rx="5"/>
    <text class="vulnerability-text" x="987" y="542">Suboptimal</text>
    <text class="vulnerability-text" x="987" y="562">Mindstate</text>
    <line class="pointer" x1="990" y1="578" x2="949" y2="631" marker-end="url(#arrowhead)"/>
  </g>

  <!-- Outcome -->
  <line class="pointer" x1="750" y1="685" x2="750" y2="894" marker-end="url(#arrowhead)"/>
  <text class="outcome" x="752" y="935">Sustained Weight Loss</text>
  <text class="outcome" x="752" y="959">Maintenance</text>
</svg>
</body>
</html>
```